Modern, upmarket label design for food product

We need a label design for a food company producing nuts with sesame and honey. In fact, we would like the words "Cashews med sesam & honning" on the label (It's in Danish and means - Cashews with sesame & honey). It should be easy for the customer to quickly understand what it is.

It is a shelf product in the competitive food industry, which is why the design should wake the feeling of 'just wanting to grab the product down from the shelves'. So, the design should stand out and have an image of a cool, modern, hip product. This being said, I love a raw & handmade look.

The company is called Pølle. Its origins are from the danish word Tiks that is a Danish slang for yummy. I have uploaded a photo of the package the products will be sold in.

Info & dimensions on bag in picture 1.
Dimensions: 6" x 9" | 15.2 cm x 22.3 cm
Capacity: 8 ounces | 250 grams (based on whole bean coffee)

Picture 2 is the same product, but has the possibility of attaching to a hanger on shelfs.

Picture 3 - I have also uploaded a photo of a product bag, where the hole is linear instead of a round hole. The designer chooses, which bag they will like to work with!

Please let me know if there are any questions!

Target Market(s)

Target market could really be any age, but the design needs to compel the target audience to pick it from the shelves. The package should signal a product you want to hold and have other people seeing you have it. The target audience is people who cares for what they buy, and typically doesn't want a low-end or budget product. They want the whole thing, meaning it has to taste good, look good etc. They are also the type of people who like to show off whatever products they buy by placing them in their houses for their guests to see. Or by uploading pictures of it on social medias.

Industry/Entity Type

It Company

Font styles to use
Other font styles liked:
• Not a must, but I like the 'Panton' script

Requirements
Must have
• My project must have the words 'Cashews med sesam & honning' on the label, so the customer will know within a second what they are looking at and buying.
Nice to have
• I am picturing the label with the words 'Cashews med sesam & honning' as a statement, again, emphasizing how the customer instantly should know what the product is. This being said, it should not be the only thing on the package and I love a raw & handmade look - which inspiration picture 5 is a great example of!
• I have uploaded photos of what I think looks good. With this said, I am not looking for a copy of those products, but see them as good inspiration. I have named the photos inspiration 1, 2, 3, 4 & 5.
• If needed, more text can be put on the label. For example 'vegan', 'laktosefri', Glutenfri', or 'Sund Snack' are great words for being used on the label.
Should not have
• The fonts on the label should not be too decorative. Personally I like an easy too read font.

```html
<!DOCTYPE html>
<html lang="da">
<head>
<meta charset="utf-8">
<title>Pølle – Cashews med sesam &amp; honning</title>
<link rel="stylesheet" href="https://fonts.googleapis.com/css2?family=Raleway:wght@500;700;800;900&display=swap">
<style>
  :root {
    --navy: #2a3140;
    --navy-deep: #232a37;
    --green: #0d6b35;
    --green-dark: #0a5a2c;
    --white: #ffffff;
    --nut-light: #d9b27c;
    --nut-mid: #b98a52;
    --nut-dark: #8a6236;
  }
  html, body {
    margin: 0;
    padding: 0;
    width: 800px;
    height: 1200px;
    overflow: hidden;
    background: var(--navy);
  }
  .label {
    position: relative;
    width: 800px;
    height: 1200px;
    background: var(--navy);
    font-family: "Raleway", "Helvetica Neue", Arial, sans-serif;
  }
  .label__art {
    position: absolute;
    inset: 0;
  }
  .brand-name {
    font-family: "Raleway", Arial, sans-serif;
    font-weight: 900;
    font-size: 104px;
    fill: var(--white);
    letter-spacing: 1px;
  }
  .product-title {
    font-family: "Raleway", Arial, sans-serif;
    font-weight: 800;
    font-size: 86px;
    fill: var(--white);
  }
  .product-flavour {
    font-family: "Raleway", Arial, sans-serif;
    font-weight: 500;
    font-size: 47px;
    fill: var(--white);
  }
  .claim-text {
    font-family: "Raleway", Arial, sans-serif;
    font-weight: 700;
    font-size: 33px;
    fill: var(--navy);
  }
  .net-weight {
    font-family: "Raleway", Arial, sans-serif;
    font-weight: 700;
    font-size: 36px;
    fill: var(--white);
  }
  .product-window {
    position: absolute;
    left: 52px;
    top: 802px;
    width: 696px;
    height: 196px;
    border-radius: 18px;
    background: linear-gradient(90deg, var(--nut-mid), var(--nut-light) 30%, var(--nut-mid) 50%, var(--nut-light) 70%, var(--nut-mid));
  }
</style>
</head>
<body>
<div class="label">
  <svg class="label__art" width="800" height="1200" viewBox="0 0 800 1200" xmlns="http://www.w3.org/2000/svg">
    <!-- frames -->
    <rect class="frame-outer" x="20" y="20" width="760" height="1160" rx="42" fill="none" stroke="var(--white)" stroke-width="5"/>
    <rect class="frame-inner" x="38" y="38" width="724" height="1124" rx="30" fill="none" stroke="var(--green)" stroke-width="4" stroke-dasharray="12 8"/>

    <!-- brand banner -->
    <path class="brand-banner" d="M193 -5 H607 V250 L400 214 L193 250 Z" fill="var(--navy)" stroke="var(--green)" stroke-width="6"/>
    <text class="brand-name" x="400" y="158" text-anchor="middle">PØLLE</text>

    <!-- top divider -->
    <g class="divider" fill="var(--white)">
      <circle cx="213" cy="320" r="5"/><circle cx="248" cy="320" r="5"/><circle cx="283" cy="320" r="5"/><circle cx="318" cy="320" r="5"/>
      <circle cx="482" cy="320" r="5"/><circle cx="517" cy="320" r="5"/><circle cx="552" cy="320" r="5"/><circle cx="587" cy="320" r="5"/>
      <path d="M356 320 L400 300 L444 320 L400 340 Z" fill="none" stroke="var(--white)" stroke-width="4"/>
      <path d="M372 320 L400 308 L428 320 L400 332 Z"/>
    </g>

    <!-- title ribbon -->
    <path class="ribbon-tail" d="M62 585 C80 560 92 520 92 470 C92 440 86 420 78 410 H112 V585 Z" fill="var(--green)"/>
    <path class="ribbon-tail" d="M738 585 C720 560 708 520 708 470 C708 440 714 420 722 410 H688 V585 Z" fill="var(--green)"/>
    <rect class="ribbon-body" x="112" y="388" width="576" height="172" rx="10" fill="var(--green)" stroke="var(--green-dark)" stroke-width="3"/>
    <text class="product-title" x="400" y="462" text-anchor="middle">CASHEWS</text>
    <text class="product-title" x="400" y="546" text-anchor="middle">MED</text>
    <text class="product-flavour" x="400" y="609" text-anchor="middle">SESAM &amp; HONNING</text>

    <!-- lower divider -->
    <g class="divider" fill="var(--white)">
      <circle cx="213" cy="668" r="5"/><circle cx="244" cy="668" r="5"/><circle cx="275" cy="668" r="5"/><circle cx="306" cy="668" r="5"/>
      <circle cx="338" cy="668" r="5"/><circle cx="369" cy="668" r="5"/><circle cx="400" cy="668" r="5"/><circle cx="431" cy="668" r="5"/>
      <circle cx="462" cy="668" r="5"/><circle cx="494" cy="668" r="5"/><circle cx="525" cy="668" r="5"/><circle cx="556" cy="668" r="5"/>
      <circle cx="587" cy="668" r="5"/>
    </g>

    <!-- claim tag -->
    <path class="claim-tag" d="M258 729 H543 L538 737 L545 745 L539 753 L546 761 L540 769 L544 777 H258 L263 769 L256 761 L262 753 L255 745 L261 737 Z" fill="var(--white)"/>
    <text class="claim-text" x="400" y="765" text-anchor="middle">Sund Snack</text>

    <!-- product window frame -->
    <rect class="window-frame" x="45" y="795" width="710" height="210" rx="24" fill="var(--navy-deep)" stroke="#3a4355" stroke-width="4"/>

    <text class="net-weight" x="400" y="1081" text-anchor="middle">8 ounces | 250 grams</text>
  </svg>
  <div class="product-window" role="img" aria-label="Ristede cashewnødder set gennem posens vindue"></div>
</div>
</body>
</html>
```